Tarrow Building Performance

Id like for my business card to be very bold and professional. Incorporating the business logo, the main services offered, and my contact info. Services are spray foam, insulation, new construction, retrofit, weatherization.

When opening this project sketch harbor was not able to upload my new logo that I picked from another recent sketch harbor project. Does anyone know how i could upload my logo onto the page for design of the business cards?

Target Market(s)

Building owners, contractors

Industry/Entity Type

Building Insulation and performance improvements

Contact Information for Business Card

Owner, Email dean@tarrowbuildingperformance.example Phone number 555-208-6147

Colors
0054AA
0677BA
7BADD7
CADEEF
E8F1F8
F0912C
F2A743
F7CA91
FBE8D2
FDF5EE

Requirements
Must have
• Services- spray foam, cellulose, mineral wool, fiberglass, air sealing, new construction, retrofit, weatherization, energy saving assesments

```html
<!DOCTYPE html>
<html lang="en">
<head>
<meta charset="utf-8">
<title>Tarrow Building Performance – Business Card</title>
<link rel="stylesheet" href="https://fonts.googleapis.com/css2?family=Montserrat:wght@400;500;600;800&family=Oswald:wght@600&display=swap">
<style>
  :root {
    --page-bg: #e9eaec;
    --card-white: #ffffff;
    --card-navy: #1c1d33;
    --brand-blue: #34b3e4;
    --brand-orange: #ee7623;
    --ink: #1a1a1a;
    --services-ink: #1c1d33;
  }
  * { box-sizing: border-box; margin: 0; padding: 0; }
  html, body { width: 1200px; height: 1200px; overflow: hidden; }
  body {
    background: var(--page-bg);
    font-family: "Montserrat", Arial, sans-serif;
    display: flex;
    flex-direction: column;
    align-items: center;
    justify-content: center;
    gap: 60px;
  }
  .card {
    position: relative;
    width: 880px;
    height: 503px;
    border-radius: 34px;
    overflow: hidden;
    box-shadow: 0 10px 30px rgba(0,0,0,.18);
  }
  .card--front { background: var(--card-white); }
  .card--back {
    background: var(--card-navy);
    display: flex;
    align-items: center;
    justify-content: center;
  }

  /* Brand name lockup */
  .brand {
    display: flex;
    align-items: center;
    gap: 16px;
    color: var(--brand-orange);
    font-weight: 800;
    text-transform: uppercase;
    line-height: 1;
  }
  .brand__mark {
    width: 22px; height: 22px;
    background: var(--brand-blue);
    flex: none;
  }
  .card--front .brand {
    position: absolute;
    top: 70px;
    right: 60px;
    font-size: 30px;
    letter-spacing: .5px;
  }
  .card--back .brand { font-size: 44px; gap: 22px; }
  .card--back .brand__mark { width: 34px; height: 34px; }

  /* Contact block */
  .contact {
    position: absolute;
    left: 64px;
    top: 230px;
  }
  .contact__name {
    color: var(--brand-blue);
    font-weight: 600;
    font-size: 34px;
    letter-spacing: .5px;
  }
  .contact__role {
    color: var(--ink);
    font-weight: 500;
    font-size: 26px;
    letter-spacing: 1px;
    margin-top: 2px;
  }
  .contact__line {
    display: flex;
    align-items: center;
    gap: 14px;
    color: var(--ink);
    font-size: 23px;
    margin-top: 10px;
    padding-left: 34px;
  }
  .contact__line svg { width: 28px; height: 28px; flex: none; }

  /* Services */
  .services {
    position: absolute;
    left: 140px;
    right: 40px;
    top: 385px;
    font-family: "Oswald", "Arial Narrow", sans-serif;
    font-weight: 600;
    font-size: 19px;
    color: var(--services-ink);
    text-transform: uppercase;
    line-height: 1.3;
  }
  .services__row { white-space: nowrap; }
  .services__dot { color: var(--brand-blue); margin: 0 4px; }

  .card__band { position: absolute; left: 0; bottom: 0; width: 100%; height: 60px; }
</style>
</head>
<body>

  <section class="card card--front" aria-label="Business card front">
    <div class="brand">
      <span class="brand__mark"></span>
      <span class="brand__name">Tarrow Building Performance</span>
    </div>

    <div class="contact">
      <p class="contact__name">DEAN TARROW</p>
      <p class="contact__role">OWNER</p>
      <p class="contact__line">
        <svg viewBox="0 0 24 24" aria-hidden="true"><path fill="#34b3e4" d="M6.6 10.8a15.1 15.1 0 0 0 6.6 6.6l2.2-2.2a1 1 0 0 1 1-.25 11.4 11.4 0 0 0 3.6.57 1 1 0 0 1 1 1V20a1 1 0 0 1-1 1A17 17 0 0 1 3 4a1 1 0 0 1 1-1h3.5a1 1 0 0 1 1 1c0 1.25.2 2.45.57 3.57a1 1 0 0 1-.25 1z"/></svg>
        555-208-6147
      </p>
      <p class="contact__line">
        <svg viewBox="0 0 24 24" aria-hidden="true"><path fill="#34b3e4" d="M2 5h20v14H2z"/><path fill="none" stroke="#fff" stroke-width="1.6" d="M2.5 5.5 12 13l9.5-7.5M2.5 18.5l7-6.5m12 6.5-7-6.5"/></svg>
        dean@tarrowbuildingperformance.example
      </p>
    </div>

    <div class="services">
      <p class="services__row"><span class="services__dot">•</span>Spray Foam <span class="services__dot">•</span>Cellulose <span class="services__dot">•</span>Mineral Wool <span class="services__dot">•</span>Fiberglass <span class="services__dot">•</span>Air Sealing</p>
      <p class="services__row"><span class="services__dot">•</span>New Construction <span class="services__dot">•</span>Retrofit <span class="services__dot">•</span>Weatherization <span class="services__dot">•</span>Energy Saving Assesments</p>
    </div>

    <svg class="card__band" viewBox="0 0 880 60" preserveAspectRatio="none" aria-hidden="true">
      <polygon points="0,48 560,26 548,60 0,60" fill="var(--brand-blue)"/>
      <polygon points="574,25 880,13 880,60 560,60" fill="var(--brand-orange)"/>
    </svg>
  </section>

  <section class="card card--back" aria-label="Business card back">
    <div class="brand">
      <span class="brand__mark"></span>
      <span class="brand__name">Tarrow Building Performance</span>
    </div>
  </section>

</body>
</html>
```